Stonebrook 720 Real Estate Investment Company

We need a business card designed for a real estate investment company named Stonebrook 720. We want to use red#f04a50, orange #f37122 and yellow #fbee3e as the color scheme. The logo colors will need to be modified from the current blue palette. I've attach VitaPathway logo example that captures the color scheme we're going for for Stonebrook 720. Looking for clean Sans Serif fonts.
Contact Information for Business Card
Daniel Furlow
Managing Partner
48317 Whitfield Lane, Suite 510
Tampa, FL 33718
813-555-4870 Mobile
dfurlow@stonebrook720.example
www.stonebrook720.example
Requirements
Must have
- Looking for creative responses.
Nice to have
- Must hit color palette... orange, red, yellow

```html
<!DOCTYPE html>
<html lang="en">
<head>
<meta charset="utf-8">
<title>Stonebrook 720 – Business Card</title>
<link rel="stylesheet" href="https://fonts.googleapis.com/css2?family=Lato:wght@400;700;900&family=Oswald:wght@500;600&display=swap">
<style>
  :root {
    --backdrop: #161616;
    --card-edge: #2a2a2a;
    --ink: #f2f2f2;
    --brand-red: #f04a50;
    --brand-orange: #f37122;
    --brand-yellow: #fbee3e;
  }
  * { box-sizing: border-box; margin: 0; padding: 0; }
  html, body {
    width: 1200px; height: 900px; overflow: hidden;
    background: var(--backdrop);
    font-family: "Lato", Arial, sans-serif;
    color: var(--ink);
  }
  .canvas { position: relative; width: 1200px; height: 900px; }
  .card {
    position: absolute; left: 270px; width: 660px; height: 377px;
    background: linear-gradient(135deg, #1b1b1b 0%, #222 60%, #2a2a2a 100%);
    border: 1px solid var(--card-edge);
    box-shadow: 0 12px 30px rgba(0,0,0,.55);
  }
  .card--front { top: 60px; }
  .card--back  { top: 483px; }

  /* front */
  .brand {
    position: absolute; top: 50%; left: 50%;
    transform: translate(-50%, -50%);
    display: flex; align-items: center; gap: 16px;
  }
  .brand__name {
    font-weight: 900; font-size: 44px; letter-spacing: .5px;
    color: var(--ink); white-space: nowrap;
  }
  .brand__dot {
    width: 22px; height: 22px; border-radius: 50%;
    background: var(--brand-orange);
  }

  /* back */
  .details {
    position: absolute; top: 128px; left: 72px;
    display: flex; align-items: center; gap: 18px;
  }
  .identity { text-align: right; }
  .identity__name {
    font-family: "Oswald", "Arial Narrow", sans-serif;
    font-weight: 600; font-size: 34px;
    letter-spacing: 1.5px; text-transform: uppercase;
    color: var(--brand-red); line-height: 1;
  }
  .identity__title { font-size: 18px; margin-top: 6px; color: var(--ink); }
  .divider { width: 2px; height: 76px; background: var(--brand-orange); }
  .contacts { list-style: none; }
  .contacts li {
    display: flex; align-items: center; gap: 10px;
    font-size: 17px; line-height: 24px; color: var(--ink); white-space: nowrap;
  }
  .contacts svg { width: 13px; height: 13px; flex: none; }
  .address {
    position: absolute; left: 72px; bottom: 54px;
    font-size: 20px; color: var(--ink); white-space: nowrap;
  }
</style>
</head>
<body>
<main class="canvas">
  <section class="card card--front" aria-label="Card front">
    <div class="brand">
      <span class="brand__name">Stonebrook 720</span>
      <span class="brand__dot" aria-hidden="true"></span>
    </div>
  </section>

  <section class="card card--back" aria-label="Card back">
    <div class="details">
      <div class="identity">
        <h1 class="identity__name">Daniel Furlow</h1>
        <p class="identity__title">Managing Partner</p>
      </div>
      <div class="divider" aria-hidden="true"></div>
      <ul class="contacts">
        <li>
          <svg viewBox="0 0 16 16" aria-hidden="true"><path fill="var(--brand-yellow)" d="M3.5 1.5l2.5 0 1.2 3.2-1.6 1.2a8 8 0 0 0 4.5 4.5l1.2-1.6 3.2 1.2v2.5c0 .8-.7 1.5-1.5 1.5A12 12 0 0 1 2 3c0-.8.7-1.5 1.5-1.5z"/></svg>
          813-555-4870
        </li>
        <li>
          <svg viewBox="0 0 16 16" aria-hidden="true"><rect x="1.5" y="3.5" width="13" height="9" fill="none" stroke="var(--brand-yellow)" stroke-width="1.5"/><path d="M1.5 3.5l6.5 5 6.5-5" fill="none" stroke="var(--brand-yellow)" stroke-width="1.5"/></svg>
          dfurlow@stonebrook720.example
        </li>
        <li>
          <svg viewBox="0 0 16 16" aria-hidden="true"><g fill="none" stroke="var(--brand-yellow)" stroke-width="1.3"><circle cx="8" cy="8" r="6.5"/><ellipse cx="8" cy="8" rx="3" ry="6.5"/><path d="M1.5 8h13M2.5 4.5h11M2.5 11.5h11"/></g></svg>
          www.stonebrook720.example
        </li>
      </ul>
    </div>
    <p class="address">48317 Whitfield Lane, Suite 510 Tampa, FL 33718</p>
  </section>
</main>
</body>
</html>
```